Letterhead Design Project

I need a simple, clean and corporate letterhead & follow-on letterhead.
The follow-on letterhead should just have the logo only.
Final File Specs:
Full Bleed Size (starting document size)
213 x 300 mm
2517 x 3544 pixels
* Finished artwork should use the full bleed dimensions for best results.
Document Trim Size (final size after being cut)
210 x 297 mm
2480 x 3508 pixels
* Please be sure to keep all text within the safe margin.
Resolution 300 DPI
Accepted file types:-
Adobe Acrobat 9 Document (*.pdf) (recommended)
Adobe Illustrator CS3 Artwork (*.ai) (recommended)
Adobe Photoshop CS3 Image (*.psd) (recommended)
Bitmap Image (*.bmp)
GIF Image (*.gif)
JPEG Image (*.jpg,*.jpeg)
Microsoft PowerPoint 2010 Document (*.ppt)
Microsoft Publisher 2010 Document (*.pub)
Microsoft Word 2010 Document (*.doc)
PCX Image (*.pcx)
PICT Image (*.pic,*.pict,*.pct)
PNG Image (*.png)
PostScript Document (*.ps)
TIF Image (*.tif,*.tiff)
Windows Enhanced Metafile (*.emf)
Windows Metafile (*.wmf)
Requirements
Must have
- My letterhead must have:-
- Logo
- ACN - 482 617 309
- address - Suite 8, 51 Hartwell Ave, Marlow Bay, NSW 2187
- phone - (02) 8371 5926
- fax - (02) 8352 6149
- email - info@brantorguard.com.au
- web - www.brantorguard.com.au
Follow-on letterhead should have the logo only

```html
<!DOCTYPE html>
<html lang="en">
<head>
<meta charset="utf-8">
<title>Brantor Asbestos &amp; Safety — Letterhead Set</title>
<link href="https://fonts.googleapis.com/css2?family=Barlow:wght@400;500;700&display=swap" rel="stylesheet">
<style>
  :root {
    --bg-centre: #ffffff;
    --bg-edge: #e2e2e4;
    --paper: #ffffff;
    --paper-edge: #a9a9ab;
    --brand-green: #8dc63f;
    --brand-green-mid: rgba(141, 198, 63, 0.55);
    --brand-green-soft: rgba(141, 198, 63, 0);
    --brand-navy: #1f2150;
    --text-dark: #2a2a2e;
  }
  html, body {
    margin: 0;
    padding: 0;
    width: 1200px;
    height: 857px;
    overflow: hidden;
  }
  body {
    position: relative;
    background: radial-gradient(ellipse 62% 60% at 50% 52%, var(--bg-centre) 62%, var(--bg-edge) 100%);
    font-family: "Barlow", "Helvetica Neue", Arial, sans-serif;
  }
  .sheet {
    position: absolute;
    top: 135px;
    width: 398px;
    height: 580px;
    background: var(--paper);
    border: 1px solid var(--paper-edge);
  }
  .sheet--first { left: 111px; }
  .sheet--follow-on { left: 651px; }

  .header-band {
    position: absolute;
    top: 0; left: 0; right: 0;
    height: 100px;
    background: linear-gradient(to bottom, var(--brand-green) 0, var(--brand-green) 3px, var(--brand-green-mid) 12px, var(--brand-green-soft) 100%);
  }

  .brand {
    position: absolute;
    left: 50%;
    transform: translateX(-50%);
    display: flex;
    flex-direction: column;
    align-items: center;
    color: var(--brand-navy);
    font-weight: 700;
  }
  .sheet--first .brand { top: 47px; }
  .sheet--follow-on .brand { top: 523px; }
  .brand__name {
    display: flex;
    align-items: center;
    gap: 4px;
    font-size: 20px;
    line-height: 1;
  }
  .brand__square {
    width: 13px;
    height: 13px;
    background: var(--brand-navy);
  }
  .brand__tagline {
    margin-top: 2px;
    font-size: 6.5px;
    letter-spacing: 0.2px;
  }

  .contact-footer {
    position: absolute;
    left: 0; right: 0;
    top: 537px;
    text-align: center;
    font-size: 6.2px;
    line-height: 9px;
    color: var(--text-dark);
  }
  .contact-footer .label {
    color: var(--brand-green);
    font-weight: 700;
  }
</style>
</head>
<body>
  <section class="sheet sheet--first" aria-label="First-page letterhead">
    <div class="header-band"></div>
    <div class="brand">
      <div class="brand__name"><span class="brand__square"></span>Brantor</div>
      <div class="brand__tagline">ASBESTOS &amp; SAFETY</div>
    </div>
    <footer class="contact-footer">
      <div><span class="label">acn:</span> 482 617 309 | <span class="label">add.:</span> Suite 8, 51 Hartwell Ave, Marlow Bay, NSW 2187 | <span class="label">tel.:</span> (02) 8371 5926 | <span class="label">fax.:</span> (02) 8352 6149</div>
      <div><span class="label">e-mail:</span> info@brantorguard.com.au | <span class="label">web:</span> www.brantorguard.com.au</div>
    </footer>
  </section>

  <section class="sheet sheet--follow-on" aria-label="Follow-on letterhead">
    <div class="brand">
      <div class="brand__name"><span class="brand__square"></span>Brantor</div>
      <div class="brand__tagline">ASBESTOS &amp; SAFETY</div>
    </div>
  </section>
</body>
</html>
```